Business Card Design for Property Development Company Director

I am looking for a professional and unforgettable business card design for our Director of our Property Development Company.
Please see attached .pptx file to find out what information to include. You don't have to follow the exact format shown in the file - I am interested to see your creative flair using the information provided.

```html
<!DOCTYPE html>
<html lang="en">
<head>
<meta charset="utf-8">
<title>Halvern Property Group – Business Card</title>
<link rel="stylesheet" href="https://fonts.googleapis.com/css2?family=Open+Sans:wght@400;600&family=Roboto:wght@700&display=swap">
<style>
  :root {
    --backdrop: #d2d5d7;
    --card: #f3f3f1;
    --brand-blue: #1b46a3;
    --ink-grey: #5a5a5a;
    --shadow: rgba(40, 45, 50, 0.18);
  }
  * { margin: 0; padding: 0; box-sizing: border-box; }
  html, body {
    width: 1200px;
    height: 1050px;
    overflow: hidden;
    background: var(--backdrop);
  }
  .canvas {
    position: relative;
    width: 1200px;
    height: 1050px;
  }
  .card {
    position: absolute;
    left: 320px;
    width: 560px;
    height: 320px;
    background: var(--card);
    box-shadow: 0 14px 30px var(--shadow);
    font-family: "Open Sans", sans-serif;
  }
  .card--front { top: 170px; }
  .card--back { top: 560px; }

  .brand {
    display: flex;
    align-items: center;
    gap: 12px;
  }
  .brand__mark {
    width: 22px;
    height: 22px;
    background: var(--brand-blue);
  }
  .brand__name {
    font-family: "Open Sans", sans-serif;
    font-weight: 600;
    color: var(--brand-blue);
    letter-spacing: 0.04em;
    text-transform: uppercase;
  }
  .card--front .brand {
    position: absolute;
    left: 50%;
    top: 50%;
    transform: translate(-50%, -50%);
  }
  .card--front .brand__name { font-size: 26px; }
  .card--front .brand__mark { width: 30px; height: 30px; }

  .card--back .brand {
    position: absolute;
    right: 48px;
    top: 150px;
  }
  .card--back .brand__name { font-size: 16px; }
  .card--back .brand__mark { width: 18px; height: 18px; }

  .contact {
    position: absolute;
    left: 48px;
    top: 44px;
  }
  .contact__name {
    font-family: "Roboto", sans-serif;
    font-weight: 700;
    font-size: 19px;
    color: var(--brand-blue);
  }
  .contact__role {
    font-size: 14px;
    color: var(--ink-grey);
    margin-bottom: 22px;
  }
  .contact__line {
    font-size: 13px;
    color: var(--ink-grey);
    line-height: 1.6;
  }
  .contact__line--gap { margin-top: 14px; }
  .contact__label { color: var(--brand-blue); }

  .licence {
    position: absolute;
    left: 48px;
    bottom: 40px;
    font-size: 13px;
    color: var(--ink-grey);
  }
</style>
</head>
<body>
<main class="canvas">
  <section class="card card--front" aria-label="Card front">
    <div class="brand">
      <span class="brand__mark"></span>
      <span class="brand__name">Halvern Property Group</span>
    </div>
  </section>

  <section class="card card--back" aria-label="Card back">
    <div class="contact">
      <p class="contact__name">Daniel Marsh</p>
      <p class="contact__role">Director</p>
      <p class="contact__line"><span class="contact__label">P:</span> 0412 630 218</p>
      <p class="contact__line">daniel@halvern.com.au</p>
      <p class="contact__line contact__line--gap">www.halvern.com.au</p>
    </div>
    <div class="brand">
      <span class="brand__mark"></span>
      <span class="brand__name">Halvern Property Group</span>
    </div>
    <p class="licence"><span class="contact__label">Real Estate Lic:</span>&nbsp; 5102386 &amp; 5102387</p>
  </section>
</main>
</body>
</html>
```